Tildens Biscuit Barn Website

I need a website for a diner/restaurant that has been established in a farming, oil and industrial community for over 15 years. The website needs to be simple in design, but that should demonstrate the mastery of skills of the designer. Our diner/restaurant is family oriented, patriotic but very rustic
Fb Address is fb.me/TildensBarn

Pictures of the restaurant

https://www.filecrate-example.net/s/qk72hdw01/Tildens_05.jpg

Pictures of About us

https://www.filecrate-example.net/sh/zm40vrt88/AboutUsPhotos

Article about Tilden's
https://www.filecrate-example.net/s/wp31nbx57/TildensBiscuitBarn1.PDF
https://www.filecrate-example.net/s/hy65lcu29/TildensBiscuitBarn2.PDF

Reason: I was slow to update with information.

Reason: I am just getting feedback to the designs posted. I wasn't sure of the limited feedback was limiting designers from submitting designs. That and running a business with 25 employees open 12 hours a day, being here 2 hours prior and 2-3 hours after makes for long days.

I've increased the first place prize and also added funds to the second and third place prizes for your effort.

I just need the files in PSD, not HTML 5 as originally requested. We can handle getting the coding part.

Ill have the contest finalized by Monday. Thanks for your patience.

Target Market(s)

Cross section of adults from 18-35 & 35-55.

Industry/Entity Type

Industrial

Font styles to use
Other font styles liked:
• ff tisa web pro or garamond premier pro

Requirements
Must have
• Must be clean, look nice and not look like an afterthought.
Nice to have
• Please see the last two documents for information about our restaurant, which was featured in our local newspaper.

```html
<!DOCTYPE html>
<html lang="en">
<head>
<meta charset="utf-8">
<title>Tilden's Biscuit Barn</title>
<link rel="stylesheet" href="https://fonts.googleapis.com/css2?family=Exo+2:ital,wght@1,800&family=Open+Sans:wght@400;600&family=Titillium+Web:wght@400;600&display=swap">
<style>
:root{
  --wood:#e9d9b0;
  --wood-dark:#dcc89a;
  --nav-blue:#3f6f86;
  --nav-red:#9b1638;
  --ink:#2a201a;
  --brand-red:#b3163f;
  --brand-blue:#2f6f8a;
  --band:#c9b999;
  --band-text:#3a3028;
  --dark:#1c1410;
  --dark-line:#3a2e26;
  --teal:#4e9bb5;
  --gold:#f3c552;
  --btn:#f6c66a;
  --light:#d9cfc2;
}
*{margin:0;padding:0;box-sizing:border-box}
html,body{width:938px;height:1200px;overflow:hidden}
body{position:relative;font-family:"Open Sans",sans-serif;background:var(--wood);color:var(--ink)}
.abs{position:absolute}

/* header */
.site-header{position:absolute;left:0;top:0;width:938px;height:157px;background:linear-gradient(180deg,#efe1bb,var(--wood-dark))}
.brand{left:66px;top:50px;display:flex;align-items:center;gap:8px}
.brand-dot{width:22px;height:22px;border-radius:50%;background:var(--brand-red)}
.brand-name{font-family:"Titillium Web",sans-serif;font-weight:600;font-size:22px;color:var(--brand-red)}
.main-nav{left:314px;top:19px;width:554px;height:53px;display:flex;background:var(--nav-blue);border:1px solid #2e566a}
.main-nav a{flex:auto;display:flex;align-items:center;justify-content:center;font-family:"Titillium Web",sans-serif;font-size:16px;color:#fff;text-decoration:none;border-right:1px solid #35627a}
.main-nav a.is-active{background:var(--nav-red);flex:0 0 80px}
.join{left:519px;top:89px;font-family:"Titillium Web",sans-serif;font-style:italic;font-weight:600;font-size:12px}
.social{left:518px;top:108px;display:flex;gap:7px}
.social span{width:19px;height:19px;background:#b5a37e}
.social span:first-child{background:var(--brand-red)}
.icon-menu{left:694px;top:87px}
.icon-shop{left:807px;top:87px;width:57px;height:56px;border:3px solid var(--ink);background:transparent}

/* hero */
.hero{left:0;top:157px;width:938px;height:488px;background:radial-gradient(ellipse at 40% 45%,#d99a45 0%,#b86a2a 45%,#6e3a18 100%)}
.hero-line{left:68px;font-family:"Exo 2",sans-serif;font-style:italic;font-weight:800;color:#fff;font-size:35px;padding:0 18px;display:flex;align-items:center;letter-spacing:.5px}
.hero-line.first{top:487px;width:480px;height:61px;background:rgba(63,111,134,.92)}
.hero-line.second{top:559px;width:296px;height:61px;background:rgba(30,24,20,.88)}

/* features */
.features{left:0;top:645px;width:938px;height:213px;background:var(--band)}
.feature{top:18px;width:189px}
.feature .photo{width:189px;height:89px}
.feature h3{margin-top:6px;font-family:"Titillium Web",sans-serif;font-weight:600;font-size:16px;color:var(--ink)}
.feature h3.accent{color:var(--brand-red)}
.feature p{margin-top:6px;font-size:9.4px;line-height:16px;color:var(--band-text)}

/* info band */
.info{left:0;top:858px;width:938px;height:269px;background:linear-gradient(90deg,#1a120e,#241a14 50%,#1a120e)}
.col{top:16px}
.col h4{font-family:"Titillium Web",sans-serif;font-weight:400;font-size:16px;color:var(--teal);padding-bottom:8px;border-bottom:1px solid var(--dark-line)}
.col p,.col li{font-size:10.5px;line-height:16px;color:var(--light)}
.btn{position:absolute;height:23px;border-radius:12px;background:var(--btn);color:var(--ink);font-size:12px;display:flex;align-items:center;justify-content:center}
.thumb{width:57px;height:57px;border-radius:50%;background:radial-gradient(circle,#e8e6e2,#8a7a6a)}
.teaser-title{font-family:"Titillium Web",sans-serif;font-weight:600;font-size:13px;color:var(--gold)}
.date{font-family:"Titillium Web",sans-serif;font-weight:600;font-size:12px;color:var(--gold)}
.more{font-style:italic;font-weight:600;font-size:9.5px;color:#fff}
.col ul{list-style:none}

/* footer */
.site-footer{left:0;top:1127px;width:938px;height:73px;background:linear-gradient(180deg,#efe1bb,var(--wood-dark))}
.foot-links{font-size:10.5px;color:var(--ink)}
.foot-links .here{color:var(--brand-red)}
.foot-brand{left:652px;top:19px;display:flex;align-items:center;gap:6px}
.foot-brand span:first-child{width:16px;height:16px;border-radius:50%;background:#8a7a66}
.foot-brand span:last-child{font-family:"Titillium Web",sans-serif;font-weight:600;font-size:14px;color:#6a5a48}
.copy{left:698px;top:1143px;font-size:10.5px}
</style>
</head>
<body>
<header class="site-header">
  <div class="abs brand"><span class="brand-dot"></span><span class="brand-name">Tilden's</span></div>
  <nav class="abs main-nav">
    <a class="is-active" href="#">Home</a><a href="#">Our History</a><a href="#">Menu</a><a href="#">Events</a><a href="#">News</a><a href="#">Contact Us</a>
  </nav>
  <div class="abs join">JOIN US</div>
  <div class="abs social"><span></span><span></span><span></span><span></span><span></span><span></span></div>
  <svg class="abs icon-menu" width="96" height="56" viewBox="0 0 96 56">
    <g fill="#2a201a">
      <rect x="3" y="4" width="3" height="14"/><rect x="8" y="4" width="3" height="14"/><rect x="13" y="4" width="3" height="14"/>
      <rect x="6" y="16" width="7" height="38" rx="3"/>
      <circle cx="48" cy="28" r="26"/>
      <ellipse cx="88" cy="16" rx="6" ry="13"/><rect x="85" y="26" width="6" height="28" rx="3"/>
    </g>
    <circle cx="48" cy="28" r="18" fill="none" stroke="#e9d9b0" stroke-width="2"/>
    <text x="48" y="32" text-anchor="middle" font-family="Titillium Web, sans-serif" font-size="11" font-weight="600" fill="#e9d9b0">MENU</text>
  </svg>
  <div class="abs icon-shop"></div>
</header>

<section class="abs hero" role="img" aria-label="Close-up photo of quesadillas, guacamole, salsa and sour cream"></section>
<div class="abs hero-line first">LOREM IPSUM DOLOR SIT</div>
<div class="abs hero-line second">CONSECTETUR</div>

<section class="abs features">
  <article class="abs feature" style="left:67px">
    <div class="photo" role="img" aria-label="Photo of two guests seated at a diner table" style="background:linear-gradient(135deg,#c9d6df,#6b5a4c)"></div>
    <h3 class="accent">Welcome to Tilden's</h3>
    <p>Lorem ipsum dolor sit amet, consectetur a adipiscing elit. Pellentesque eget ipsum ac ex dignissim convallis ac id felis Pelltesque eget ipsum ac ex dignissim.</p>
  </article>
  <article class="abs feature" style="left:272px">
    <div class="photo" role="img" aria-label="Photo of condiments and cups on a diner table" style="background:linear-gradient(135deg,#e7eef2,#9aa6b0 60%,#b0443a)"></div>
    <h3>Our Special Coffee</h3>
    <p>Lorem ipsum dolor sit amet, consectetur a adipiscing elit. Pellentesque eget ipsum ac ex dignissim convallis ac id felis Pelltesque eget ipsum ac ex dignissim.</p>
  </article>
  <article class="abs feature" style="left:477px">
    <div class="photo" role="img" aria-label="Photo of a plated sandwich served in the dining room" style="background:linear-gradient(135deg,#8a6a3a,#e8d2a8 55%,#c47a3a)"></div>
    <h3>Our Menu</h3>
    <p>Lorem ipsum dolor sit amet, consectetur a adipiscing elit. Pellentesque eget ipsum ac ex dignissim convallis ac id felis Pelltesque eget ipsum ac ex dignissim.</p>
  </article>
  <article class="abs feature" style="left:682px">
    <div class="photo" role="img" aria-label="Photo of guests in vintage costume at an event" style="background:linear-gradient(135deg,#8a8078,#d8c8b4 50%,#5a6a8a)"></div>
    <h3>Best news</h3>
    <p>Lorem ipsum dolor sit amet, consectetur a adipiscing elit. Pellentesque eget ipsum ac ex dignissim convallis ac id felis Pelltesque eget ipsum ac ex dignissim.</p>
  </article>
</section>

<section class="abs info">
  <div class="abs col" style="left:68px;width:180px">
    <h4>Check Your Balance</h4>
    <p style="margin-top:18px">Find out how much Grangeway's goodness you have left on your card. You're just a click away!</p>
    <p style="margin-top:30px">Find out how much Grangeway's goodness you have left on your card. You're just a click away!</p>
  </div>
  <span class="btn" style="left:67px;top:214px;width:97px">Click Hear</span>

  <div class="abs col" style="left:281px;width:182px">
    <h4>View Menu</h4>
    <div style="display:flex;gap:10px;margin-top:14px">
      <div class="thumb" role="img" aria-label="Photo of a coffee cup"></div>
      <div><div class="teaser-title">Lorem ipsum</div><p>Lorem ipsum dolor sit amet, consectetur adipi-</p></div>
    </div>
    <div style="display:flex;gap:10px;margin-top:18px">
      <div class="thumb" role="img" aria-label="Photo of a coffee cup"></div>
      <div><div class="teaser-title">Lorem ipsum</div><p>Lorem ipsum dolor sit amet, consectetur adipi-</p></div>
    </div>
  </div>
  <span class="btn" style="left:280px;top:214px;width:113px">See our menu</span>

  <div class="abs col" style="left:522px;width:156px">
    <h4>Latest News</h4>
    <p style="margin-top:14px">Grangeway's Selected Among Top 50 Franchises for Veterans</p>
    <div style="display:flex;justify-content:space-between;align-items:center;margin-top:2px"><span class="date">7/27/2013</span><span class="more">Read more</span></div>
    <p style="margin-top:24px">Grangeway's Selected Among Top 50 Franchises for Veterans</p>
    <div style="display:flex;justify-content:space-between;align-items:center;margin-top:2px"><span class="date">7/27/2013</span><span class="more">Read more</span></div>
  </div>
  <span class="btn" style="left:521px;top:214px;width:97px">Read more</span>

  <div class="abs col" style="left:739px;width:133px">
    <h4>Resources</h4>
    <ul style="margin-top:14px">
      <li style="margin-bottom:8px">Download a Menu</li>
      <li style="margin-bottom:8px">Employment Opportunities</li>
      <li style="margin-bottom:8px">Join the E-Club</li>
      <li style="margin-bottom:8px">Grangeway's New Book</li>
      <li>Our Official Photo Gallery</li>
    </ul>
  </div>
</section>

<footer class="abs site-footer">
  <div class="abs foot-links" style="left:67px;top:19px"><span class="here">Home</span> &nbsp;/&nbsp; Our History &nbsp;/&nbsp; Menu &nbsp;/&nbsp; Events &nbsp;/&nbsp; News &nbsp;/&nbsp; Contact Us</div>
  <div class="abs foot-links" style="left:67px;top:42px">Terms of Use &nbsp;/&nbsp; Privacy Policy &nbsp;/&nbsp; Site map</div>
  <div class="abs foot-brand"><span></span><span>Tilden's</span></div>
</footer>
<div class="abs copy foot-links" style="left:720px">© 2013 Tilden's. All rights reserved.</div>
</body>
</html>
```